Firm of surveyors needs a professional yet friendly looking flyer

Our company offers help to landlords who have a phone mast on their property. We help them to negotiate the best rent and lease terms. There are so many landlords who don't seek professional advice because they don't know it's available. We want to send them a flyer which is informative, looks professional but also friendly so it prompts them to call us. I have attached the wording and some pictures but have more I can send but they were too large to attach.

Target Market(s)

Ranges from farmers to large corporations and land owners

Industry/Entity Type

Surveyor

Font styles to use
Sans Serif

Colors
acd136
9bcb3c
000000
ffffff
606060
848484

Requirements
Must have
• Must be clear, must give a professional look, must include pictures, must include our logo, must use our colour scheme (or variations of it). Ideally, I would like a try-fold design if possible.
Nice to have
• I would like there to be stand out lines to catch the readers eye (I have included some on the wording document). I would like a clean and modern design
Should not have
• Should not be too fussy

```html
<!DOCTYPE html>
<html lang="en">
<head>
<meta charset="utf-8">
<title>Signalfield Surveyors – Tri-fold Flyer</title>
<link href="https://fonts.googleapis.com/css2?family=Open+Sans:wght@400;600&family=Roboto:wght@400;700&family=Titillium+Web:wght@400;600;700&display=swap" rel="stylesheet">
<style>
:root{
  --green-panel:#466e31;
  --green-text:#5b8a2d;
  --green-bright:#9bcb3c;
  --black:#000;
  --white:#fff;
  --grey-dark:#3a3a3a;
  --grey:#606060;
  --sky-top:#1f5fb8;
  --sky-bottom:#7fb1e6;
  --page-bg:#e6e6e6;
}
*{margin:0;padding:0;box-sizing:border-box}
html,body{width:797px;height:1200px;overflow:hidden;background:var(--page-bg)}
body{position:relative;font-family:'Open Sans',sans-serif;color:var(--grey-dark)}
.sheet{position:absolute;left:56px;width:678px;height:528px;background:var(--white);box-shadow:0 2px 6px rgba(0,0,0,.25)}
.sheet--outside{top:58px}
.sheet--inside{top:606px}
.block{position:absolute}

/* outside */
.intro{left:0;top:0;width:228px;height:157px;background:var(--black);padding:20px 0 0 20px;font-family:'Titillium Web',sans-serif}
.intro__q{color:var(--white);font-weight:600;font-size:17.5px;line-height:21px}
.intro__a{color:var(--green-bright);font-weight:600;font-size:13.5px;line-height:21px;margin-top:10px}
.intro__a .big{font-size:19px}
.contact{left:228px;top:0;width:222px;height:157px;padding:22px 0 0 20px;font-size:9px;line-height:14px;color:var(--grey-dark)}
.contact__name{font-family:'Roboto',sans-serif;font-weight:700;color:var(--green-text);font-size:12px;margin-bottom:9px}
.contact__addr{margin-bottom:7px}
.contact__row{display:flex;align-items:center;gap:5px}
.contact__row svg{width:7px;height:7px;fill:var(--grey-dark)}
.contact__web{color:var(--green-text);font-weight:600}
.brand{display:flex;align-items:center;gap:7px;font-family:'Titillium Web',sans-serif;font-weight:700;color:var(--green-text)}
.brand__dot{width:14px;height:14px;border-radius:50%;background:var(--green-bright);flex:none}
.brand--cover{left:450px;top:0;width:228px;height:157px;justify-content:center;font-size:19px}
.services{left:0;top:157px;width:228px;height:268px;background:var(--green-panel);padding:16px 0 0 21px}
.services__title{font-family:'Titillium Web',sans-serif;font-weight:600;font-size:22px;color:var(--white);letter-spacing:.3px;margin-bottom:6px}
.services__list{list-style:none}
.services__list li{font-family:'Titillium Web',sans-serif;font-weight:600;font-size:11.5px;color:var(--white);line-height:18.6px;display:flex;align-items:center}
.services__list li::before{content:"";width:8px;height:8px;border-radius:50%;background:var(--black);margin-right:7px;flex:none}
.photo-sky{background:linear-gradient(180deg,var(--sky-top),var(--sky-bottom))}
.photo-tower{left:228px;top:157px;width:222px;height:268px}
.photo-field{left:450px;top:157px;width:228px;height:268px;background:linear-gradient(180deg,#6b9ad4 0%,#b9cfe8 62%,#6e8e3e 72%,#4f7a2c 100%)}
.exclusive{left:467px;top:176px;font-family:'Roboto',sans-serif;font-size:16px;line-height:24px;color:var(--black)}
.brand--footer{left:0;top:425px;width:228px;height:103px;justify-content:center;font-size:17px}
.cta{left:228px;top:425px;width:222px;height:103px;background:var(--black);text-align:center;padding-top:6px}
.cta__phone{font-family:'Roboto',sans-serif;font-weight:700;font-size:26px;color:var(--green-bright);letter-spacing:.5px}
.cta__rule{width:160px;height:1px;background:#777;margin:3px auto 8px}
.cta__call{font-family:'Roboto',sans-serif;font-size:18px;color:var(--white);letter-spacing:.5px}
.cta__note{font-family:'Roboto',sans-serif;font-size:9px;color:var(--white);margin-top:3px}
.surveyors{left:450px;top:425px;width:228px;height:103px;padding:18px 15px 0 10px;text-align:right;font-family:'Roboto',sans-serif;font-size:13px;line-height:17.5px;color:var(--green-text)}

/* inside */
.body-col{width:197px;font-size:6.6px;line-height:10.9px;text-align:justify;color:var(--grey-dark)}
.body-col p{margin-bottom:10px}
.body-col h2{font-family:'Roboto',sans-serif;font-weight:400;font-size:12.5px;color:var(--green-text);margin:4px 0 9px;text-align:left}
.col-left{left:17px;top:22px}
.col-right{left:466px;top:22px}
.brand--inside{left:228px;top:0;width:222px;height:100px;justify-content:center;font-size:17px}
.pitch{left:228px;top:100px;width:222px;height:428px;background:var(--green-panel)}
.photo-mast{left:242px;top:106px;width:193px;height:252px}
.pitch__text{left:245px;top:366px;color:var(--white);font-family:'Titillium Web',sans-serif;font-weight:700}
.pitch__title{font-size:22px;line-height:25px;margin-bottom:12px}
.pitch__sub{font-size:13px;line-height:17px}
.pitch__sub+.pitch__sub{margin-top:7px}
.col-right .links{margin-top:22px;text-align:left}
.links__mail{color:var(--green-text);font-size:9px}
.links__web{color:var(--green-text);font-weight:600;font-size:12px;margin-top:3px}
</style>
</head>
<body>

<section class="sheet sheet--outside">
  <div class="block intro">
    <p class="intro__q">Unsure whether you are getting the best rent?</p>
    <p class="intro__a"><span class="big">We can help you</span> to<br>achieve the best sale price,<br><span class="big">quickly</span></p>
  </div>

  <div class="block contact">
    <p class="contact__name">Signalfield Surveyors Ltd</p>
    <p class="contact__addr">Unit 4 Beacon Court, Hollin Business Park,<br>Shropshire, SY9 2QT.</p>
    <p class="contact__row"><svg viewBox="0 0 10 10"><rect x="1" y="3" width="8" height="6"/><rect x="3" y="0" width="4" height="3"/></svg>01632 960418</p>
    <p class="contact__row"><svg viewBox="0 0 10 10"><path d="M2 0h2l1 3-1.5 1a6 6 0 0 0 2.5 2.5L7 5l3 1v2c0 1-1 2-2 2A8 8 0 0 1 0 2c0-1 1-2 2-2z"/></svg>01632 960419</p>
    <p class="contact__row"><svg viewBox="0 0 10 10"><path d="M0 2h10v6H0z M0 2l5 3 5-3" /></svg>hello@signalfieldsurveyors.co.uk</p>
    <p class="contact__row contact__web"><svg viewBox="0 0 10 10"><circle cx="5" cy="5" r="4.5"/></svg>www.signalfieldsurveyors.co.uk</p>
  </div>

  <div class="block brand brand--cover"><span class="brand__dot"></span>Signalfield Surveyors</div>

  <div class="block services">
    <h2 class="services__title">OUR SERVICES</h2>
    <ul class="services__list">
      <li>Rent Reviews</li>
      <li>Lease Renewals</li>
      <li>Network Consolidation Issues</li>
      <li>Site Shares</li>
      <li>Rent Protection</li>
      <li>Equipment Upgrades</li>
      <li>Mast Removals / Decommissioning</li>
      <li>Mast Sales and Marketing</li>
      <li>Land Marketing for Masts</li>
      <li>Mast Management and Portfolios</li>
      <li>Safety Testing</li>
    </ul>
  </div>

  <div class="block photo-tower photo-sky" role="img" aria-label="Photo of a rooftop phone mast with antennas against a blue sky"></div>
  <div class="block photo-field" role="img" aria-label="Photo of a lattice phone mast standing in green farmland"></div>
  <p class="block exclusive">We act<br>EXCLUSIVELY<br>for landloards<br>on ALL phone<br>mast matters</p>

  <div class="block brand brand--footer"><span class="brand__dot"></span>Signalfield Surveyors</div>

  <div class="block cta">
    <p class="cta__phone">01632 960418</p>
    <div class="cta__rule"></div>
    <p class="cta__call">CALL US NOW</p>
    <p class="cta__note">FOR A FREE, NO OBLIGATION CHAT</p>
  </div>

  <p class="block surveyors">Our expert surveyors will be happy to help you understand proposed changes and what they could mean for you</p>
</section>

<section class="sheet sheet--inside">
  <div class="block body-col col-left">
    <p>Signalfield Surveyors is a firm of telecoms surveyors with over 15 years' experience of dealing with mobile phone mast operators. We have built up a massive database of thousands of comparable mobile phone mast deals to aid us in our telecoms negotiations. All our surveyors have spent time working for phone mast operators and know the industry inside out. We now work exclusively for landlords, fighting your corner, ensuring our landlords get the highest rents and best lease terms available in the market place.</p>
    <p>Many of the original mobile phone mast leases / agreements are now coming up for renewal. This is an ideal opportunity for landlords to achieve the best deal. We are currently offering to review telecoms leases for free and provide landlords with our recommendations. If you would like to take us up on this free no obligation offer, send a copy of your agreement and any recent correspondence to us, either via post or email using the details on this flyer. Please also provide us with your name, contact number and let us know the current rent you are achieving so we can see if there is room for improvement. Once we have received this, one of our surveyors will give you a call when convenient to talk through your lease with you, highlighting anything we feel needs addressing, any opportunity to increase the rent, or to discuss a specific issue you are having with your mast (i.e. an upgrade request).</p>
    <p>Recently, operators have been attempting to cut costs by reducing rents. They are joining forces in an effort to drive rents down. Many landlords are contacting us after receiving a letter from the operators / operator's agent, telling them they must accept a rent reduction or risk losing their site. In the majority of cases, Signalfield Surveyors can prevent this from occurring and protect the landlord's rental income.</p>
    <h2>Sell Your Phone Mast</h2>
    <p>We can also assist landlords in selling their phone mast. We have strong links with many large investors who regularly purchase the freehold or leasehold interest of masts and will pay a cash lump sum, often, even hundreds of thousands of pounds. This can be done in a matter of weeks</p>
  </div>

  <div class="block brand brand--inside"><span class="brand__dot"></span>Signalfield Surveyors</div>
  <div class="block pitch"></div>
  <div class="block photo-mast photo-sky" role="img" aria-label="Photo of a white monopole phone mast with antennas against a blue sky"></div>
  <div class="block pitch__text">
    <p class="pitch__title">Interested in<br>selling your site?</p>
    <p class="pitch__sub">Or already have an offer?</p>
    <p class="pitch__sub">We can help you to achieve<br>the best sale price,<br>quickly</p>
  </div>

  <div class="block body-col col-right">
    <p>and the cash is yours to spend however you like, regardless of whether the mast stays for the duration of the investors leasehold or not. We can negotiate flexible terms, such as a buyback option so please call us today to discuss.</p>
    <h2>Getting A Phone Mast</h2>
    <p>If you don't currently have a mast located on your land but are interested in receiving thousands of pounds a year in rental income, or you have a redundant mast you would like to market, we offer a free advertising service on our website. We will market your land to phone mast operators with a view to having a mast located there. Please visit the 'Advertise My Site' link on our website to take advantage of this service.</p>
    <h2>The Current Telecoms Climate</h2>
    <p>The telecoms market, in relation to mobile phone masts, is going through some huge changes. Operators are combining to cut costs. We have already seen Crestline join forces with Telvane and Orbis form a jointly owned company with Voxen called JNIL. More recently, Telvane and Amberline have merged to form Allreach Networks Ltd to become the new network leader. What this can mean for the landlord is changes to their site and potentially the loss of income. It can all be very confusing but don't worry, this is where we can help. We know the telecoms industry and understand how a new situation may affect a landlord, therefore, allowing us to provide the best advice on protecting your asset.</p>
    <p>In April 2017, the Government introduced the Digital Economy Act. This sets out significant changes for landlords, including the way rents are calculated. We have already seen operators contact landlords, trying to reduce their rent in light of this new law. We are working alongside specialist telecoms solicitors to try to reduce the potential negative impact on landlords.</p>
    <div class="links">
      <p class="links__mail">hello@signalfieldsurveyors.co.uk</p>
      <p class="links__web">www.signalfieldsurveyors.co.uk</p>
    </div>
  </div>
</section>

</body>
</html>
```